Talent Management Company Needs Business Cards

Using one of the logos provided (attached) K&R Talent Collective needs a business card designed.
Please visit our website for more information about us-

www.krtalentcollective.example

The face should feature a dramatic presentation of the logo with the back being reserved for our professional information which is:

The information should be:
Dorian T. Vickers
C.E.O
Email: dtvickers@krtalentcollective.example
Mobile: 555-804-2917
Website: www.krtalentcollective.example

Marcus L. Vickers
Director of Public Relations
Email: mlvickers@krtalentcollective.example
Mobile: 555-806-3350

Jules R. Hampton
Director of Client Development
Email: jhampton@krtalentcollective.example

Simon Hurlock
Director of Brand Development
Email: shurlock@krtalentcollective.example

Would like the logo to have color. I would like to see one side red or black and the other side white but if it looks better in either black or red that would be fine to but would like to see how it comes out.

Please feel free to message me and if you would like just the icon alone I have other image files that I can send as well.

Target Market(s)

Professional Athletes, coaches, entertainers age 18-35 but also must be accepted in the business community

Industry/Entity Type

Business

Requirements
Must have
• 1) Use the logo
2) Double sided
3) Distinctive
Nice to have
• Small simple images for telephone, e-mail, and Url.

```html
<!DOCTYPE html>
<html lang="en">
<head>
<meta charset="utf-8">
<title>K&amp;R Talent Collective — Business Cards</title>
<link rel="stylesheet" href="https://fonts.googleapis.com/css2?family=Arimo:wght@400;700&display=swap">
<style>
  :root {
    --page: #ffffff;
    --red-hi: #e51d28;
    --red-mid: #c3121c;
    --red-deep: #6e0006;
    --black-hi: #262626;
    --black-deep: #000000;
    --ink: #231f20;
    --white: #ffffff;
    --rule-light: #d9d9d9;
    --rule-dark: #2b2b2b;
    --shadow: rgba(0,0,0,0.28);
  }
  * { box-sizing: border-box; margin: 0; padding: 0; }
  html, body {
    width: 1200px; height: 901px; overflow: hidden;
    background: var(--page);
    font-family: "Arimo", Arial, sans-serif;
  }
  .canvas { position: relative; width: 1200px; height: 901px; }

  .card {
    position: absolute; width: 545px; height: 310px; overflow: hidden;
    box-shadow: 3px 5px 8px var(--shadow);
  }
  .card--front { left: 335px; top: 98px;
    background: radial-gradient(ellipse 70% 85% at 50% 30%, var(--red-hi) 0%, var(--red-mid) 55%, var(--red-deep) 100%); }
  .card--back-dark { left: 23px; top: 474px; }
  .card--back-light { left: 632px; top: 474px; }

  .front__mark {
    position: absolute; left: 242px; top: 88px; width: 60px; height: 60px;
    border-radius: 50%; background: var(--white);
  }
  .front__name {
    position: absolute; left: 0; right: 0; top: 170px; text-align: center;
    color: var(--white); font-weight: 700; font-size: 30px; letter-spacing: 0.5px;
  }
  .front__url {
    position: absolute; left: 0; right: 0; top: 267px; text-align: center;
    color: var(--white); font-size: 14px;
  }

  .back__top { position: absolute; left: 0; top: 0; width: 100%; height: 192px; }
  .card--back-dark .back__top {
    background: radial-gradient(ellipse 70% 100% at 50% 20%, var(--black-hi) 0%, var(--black-deep) 100%); }
  .card--back-light .back__top { background: var(--white); }

  .brand__mark {
    position: absolute; left: 246px; top: 44px; width: 52px; height: 52px;
    border-radius: 50%; background: var(--red-hi);
  }
  .brand {
    position: absolute; left: 0; right: 0; top: 140px; text-align: center;
    font-size: 23px; font-weight: 400; letter-spacing: 0.3px; white-space: nowrap;
  }
  .card--back-dark .brand { color: var(--white); }
  .card--back-light .brand { color: var(--ink); }

  .back__rule { position: absolute; left: 0; top: 192px; width: 100%; height: 9px; }
  .card--back-dark .back__rule { background: linear-gradient(180deg, #9a9a9a, #5a5a5a); }
  .card--back-light .back__rule { background: linear-gradient(90deg, var(--rule-light), #8a8a8a 60%, var(--rule-dark)); }

  .back__band {
    position: absolute; left: 0; top: 201px; width: 100%; height: 109px;
    background: radial-gradient(ellipse 60% 120% at 55% 40%, var(--red-hi) 0%, var(--red-mid) 55%, var(--red-deep) 100%);
    color: var(--white);
  }
  .person { position: absolute; right: 335px; top: 33px; text-align: right; }
  .person__name { font-weight: 700; font-size: 15px; white-space: nowrap; }
  .person__title { font-size: 13px; margin-top: 3px; }
  .divider { position: absolute; left: 224px; top: 20px; width: 1px; height: 66px; background: var(--white); }
  .contacts { position: absolute; left: 238px; top: 26px; list-style: none; font-size: 13.5px; line-height: 18.5px; }
  .contacts li { display: flex; align-items: center; gap: 8px; white-space: nowrap; }
  .contacts svg { width: 11px; height: 11px; flex: none; }
</style>
</head>
<body>
<main class="canvas">

  <section class="card card--front" aria-label="Card front">
    <div class="front__mark"></div>
    <p class="front__name">K&amp;R Talent Collective</p>
    <p class="front__url">www.krtalentcollective.example</p>
  </section>

  <section class="card card--back-dark" aria-label="Card back, dark version">
    <div class="back__top">
      <div class="brand__mark"></div>
      <p class="brand">K&amp;R TALENT COLLECTIVE</p>
    </div>
    <div class="back__rule"></div>
    <div class="back__band">
      <div class="person">
        <p class="person__name">Dorian T. Vickers</p>
        <p class="person__title">C.E.O</p>
      </div>
      <div class="divider"></div>
      <ul class="contacts">
        <li><svg viewBox="0 0 12 12"><rect x="3" y="0.5" width="6" height="11" rx="1" fill="none" stroke="#fff" stroke-width="1.2"/><rect x="4.3" y="2" width="3.4" height="5.5" fill="#fff"/></svg>555-804-2917</li>
        <li><svg viewBox="0 0 12 12"><rect x="0.5" y="2.5" width="11" height="7.5" fill="#fff"/><path d="M0.5 2.5 L6 7 L11.5 2.5" fill="none" stroke="#c3121c" stroke-width="1"/></svg>dtvickers@krtalentcollective.example</li>
        <li><svg viewBox="0 0 12 12"><circle cx="6" cy="6" r="5.3" fill="#fff"/><path d="M0.7 6 H11.3 M6 0.7 V11.3 M6 0.7 C3 3 3 9 6 11.3 M6 0.7 C9 3 9 9 6 11.3" fill="none" stroke="#c3121c" stroke-width="0.8"/></svg>www.krtalentcollective.example</li>
      </ul>
    </div>
  </section>

  <section class="card card--back-light" aria-label="Card back, light version">
    <div class="back__top">
      <div class="brand__mark"></div>
      <p class="brand">K&amp;R TALENT COLLECTIVE</p>
    </div>
    <div class="back__rule"></div>
    <div class="back__band">
      <div class="person">
        <p class="person__name">Dorian T. Vickers</p>
        <p class="person__title">C.E.O</p>
      </div>
      <div class="divider"></div>
      <ul class="contacts">
        <li><svg viewBox="0 0 12 12"><rect x="3" y="0.5" width="6" height="11" rx="1" fill="none" stroke="#fff" stroke-width="1.2"/><rect x="4.3" y="2" width="3.4" height="5.5" fill="#fff"/></svg>555-804-2917</li>
        <li><svg viewBox="0 0 12 12"><rect x="0.5" y="2.5" width="11" height="7.5" fill="#fff"/><path d="M0.5 2.5 L6 7 L11.5 2.5" fill="none" stroke="#c3121c" stroke-width="1"/></svg>dtvickers@krtalentcollective.example</li>
        <li><svg viewBox="0 0 12 12"><circle cx="6" cy="6" r="5.3" fill="#fff"/><path d="M0.7 6 H11.3 M6 0.7 V11.3 M6 0.7 C3 3 3 9 6 11.3 M6 0.7 C9 3 9 9 6 11.3" fill="none" stroke="#c3121c" stroke-width="0.8"/></svg>www.krtalentcollective.example</li>
      </ul>
    </div>
  </section>

</main>
</body>
</html>
```